Tidewell Recovery Business Card Design

Professional and clean design. The design colors should flow with the logo. Two-sided card with the website on the back which is:

www.TidewellRecovery.example.

"Specializing in Water Damage Restoration"

On the front I need the name, email, phone, and logo.

Name: Dorian Vashti
Email: Dorian@TidewellRecovery.example
Phone: 555-318-2046 for now

I only have the Preview and Thumbnail right now but should have the source files uploaded within a day or two.

Target Market(s)

Flood victims, home owners with water damage from busted pipes etc...

Industry/Entity Type

Business

Contact Information for Business Card

Name: Dorian Vashti

Font styles to use
Serif
Sans Serif

```html
<!DOCTYPE html>
<html lang="en">
<head>
<meta charset="utf-8">
<title>Tidewell Recovery Business Card</title>
<link href="https://fonts.googleapis.com/css2?family=Tinos:wght@400;700&display=swap" rel="stylesheet">
<style>
  :root {
    --backdrop: #2b2c2e;
    --card: #f7f8f8;
    --ink: #3a3a3a;
    --brand: #2a9ad6;
    --name-blue: #1fa8e4;
    --wave-light: #5cc2ec;
    --wave-pale: #7fd0f0;
    --wave-deep: #2a8fd0;
    --seam: #c9cfd3;
  }
  * { margin: 0; padding: 0; box-sizing: border-box; }
  html, body { width: 1200px; height: 900px; overflow: hidden; }
  body {
    background: var(--backdrop);
    font-family: "Tinos", "Times New Roman", serif;
    position: relative;
  }
  .card {
    position: absolute;
    left: 250px;
    width: 700px;
    height: 400px;
    background: var(--card);
    overflow: hidden;
  }
  .card--back { top: 40px; }
  .card--front { top: 460px; }
  .card__waves { position: absolute; inset: 0; width: 700px; height: 400px; }

  .brand {
    position: absolute;
    display: flex;
    flex-direction: column;
    align-items: center;
    gap: 12px;
  }
  .brand__dot {
    width: 60px; height: 60px;
    border-radius: 50%;
    background: var(--brand);
  }
  .brand__name {
    color: var(--brand);
    font-weight: 400;
    font-size: 34px;
    letter-spacing: 3px;
    text-transform: uppercase;
    white-space: nowrap;
  }
  .card--back .brand { right: 40px; top: 28px; }
  .card--front .brand { left: 60px; top: 120px; }

  .tagline {
    position: absolute;
    left: 60px;
    top: 172px;
    color: var(--ink);
    font-size: 19px;
    line-height: 1.6;
  }
  .tagline__web { display: block; padding-left: 60px; font-size: 17px; }

  .contact {
    position: absolute;
    left: 370px;
    top: 62px;
    color: var(--ink);
  }
  .contact__name {
    color: var(--name-blue);
    font-weight: 700;
    font-size: 24px;
    letter-spacing: 0.5px;
    text-transform: uppercase;
    margin-bottom: 12px;
  }
  .contact__line {
    display: flex;
    align-items: center;
    gap: 8px;
    font-size: 17px;
    line-height: 1.6;
    white-space: nowrap;
  }
  .contact__icon { width: 14px; height: 14px; flex: none; fill: var(--brand); }
</style>
</head>
<body>

<section class="card card--back" aria-label="Card back">
  <svg class="card__waves" viewBox="0 0 700 400" aria-hidden="true">
    <path d="M0,400 L0,330 C170,340 360,320 470,260 C560,210 620,185 700,175 L700,400 Z" fill="var(--wave-light)"/>
    <path d="M0,318 C160,328 350,310 460,248 C555,198 615,172 700,163 L700,175 C620,185 560,210 470,260 C360,320 170,340 0,330 Z" fill="var(--seam)"/>
    <path d="M0,290 C150,296 300,282 420,248 L428,254 C310,302 150,312 0,312 Z" fill="var(--wave-deep)"/>
    <path d="M700,205 C620,215 560,240 480,285 C390,335 220,352 0,362 L0,400 L700,400 Z" fill="var(--wave-pale)" opacity="0.55"/>
  </svg>
  <div class="brand">
    <span class="brand__dot"></span>
    <span class="brand__name">Tidewell Recovery</span>
  </div>
  <p class="tagline">
    <span class="tagline__web">www.TidewellRecovery.example.</span>
    Specializing in Water Damage Restoration
  </p>
</section>

<section class="card card--front" aria-label="Card front">
  <svg class="card__waves" viewBox="0 0 700 400" aria-hidden="true">
    <path d="M350,310 C480,295 600,250 650,170 L700,120 L700,170 C640,270 500,305 350,310 Z" fill="var(--wave-deep)"/>
    <path d="M130,400 C230,340 420,340 540,310 C630,285 680,210 700,180 L700,400 Z" fill="var(--wave-light)"/>
    <path d="M130,400 C230,340 420,340 540,310 C630,285 680,210 700,180 L700,190 C682,220 632,294 542,318 C422,348 236,348 140,400 Z" fill="var(--seam)"/>
  </svg>
  <div class="brand">
    <span class="brand__dot"></span>
    <span class="brand__name">Tidewell Recovery</span>
  </div>
  <div class="contact">
    <p class="contact__name">Dorian Vashti</p>
    <p class="contact__line">
      <svg class="contact__icon" viewBox="0 0 16 16" aria-hidden="true"><path d="M2 6c0-2 3-4 6-4s6 2 6 4l-3 1-1-2H6L5 7 2 6zm2 2h8l2 6H2l2-6z"/></svg>
      555-318-2046
    </p>
    <p class="contact__line">
      <svg class="contact__icon" viewBox="0 0 16 16" aria-hidden="true"><path d="M1 4h14v9H1zM1 4l7 5 7-5" stroke="#fff" stroke-width="1"/></svg>
      Dorian@TidewellRecovery.example
    </p>
  </div>
</section>

</body>
</html>
```